TPR Services

Kitchen installations/ carpentry / labour hire

Target Market(s)

Building companys

Industry/Entity Type

Carpentry

Contact Information for Business Card

Director Ruairi Dempsey
Phone no 0427516092
Email ruairidempsey@tprservices-example.com.au

Requirements
Nice to have
• A finished kitchen on one side in the background I would like my company name in big writing and my name in small writing so on one side I would like tpr services and on the other side have my details with the picture of the kitchen in the back round
Should not have
• Fork and spoons

```html
<!DOCTYPE html>
<html lang="en">
<head>
<meta charset="utf-8">
<title>TPR Services – Business Card</title>
<link href="https://fonts.googleapis.com/css2?family=Roboto:wght@300;400;700;900&display=swap" rel="stylesheet">
<style>
  :root {
    --stage: #2b2c2f;
    --card-black: #0d0d0d;
    --ink: #111111;
    --paper: #f4f4f4;
    --white: #ffffff;
    --soft-grey: #d9d9d9;
    --band-text: #e6e6e6;
  }
  * { margin: 0; padding: 0; box-sizing: border-box; }
  html, body {
    width: 1200px;
    height: 900px;
    overflow: hidden;
    background: var(--stage);
    font-family: "Roboto", Arial, sans-serif;
  }
  .stage {
    position: relative;
    width: 1200px;
    height: 900px;
  }
  .card {
    position: absolute;
    top: 300px;
    width: 525px;
    height: 300px;
    border-radius: 26px;
    overflow: hidden;
    box-shadow: 0 14px 30px rgba(0,0,0,0.45);
  }

  /* Details side */
  .card--details {
    left: 50px;
    background: var(--paper);
  }
  .kitchen-photo {
    position: absolute;
    left: 0; top: 0;
    width: 100%;
    height: 236px;
    background:
      linear-gradient(180deg, rgba(255,255,255,0.55) 0%, rgba(255,255,255,0.2) 60%, rgba(255,255,255,0.5) 100%),
      linear-gradient(90deg, #cfcfcf 0%, #8e8e8e 30%, #5a5a5a 50%, #bdbdbd 75%, #ececec 100%);
  }
  .details {
    position: absolute;
    left: 170px;
    top: 34px;
    width: 330px;
    text-align: center;
    color: var(--ink);
  }
  .details__name {
    font-weight: 900;
    font-size: 27px;
    letter-spacing: 0.3px;
    text-transform: uppercase;
  }
  .details__role {
    font-weight: 400;
    font-size: 19px;
    margin-top: 2px;
  }
  .details__rule {
    width: 150px;
    height: 2px;
    background: var(--ink);
    margin: 18px auto 18px;
  }
  .details__phone,
  .details__email {
    font-weight: 400;
    font-size: 16.5px;
    line-height: 1.4;
  }
  .services-band {
    position: absolute;
    left: 0; bottom: 0;
    width: 100%;
    height: 64px;
    background: var(--card-black);
    color: var(--band-text);
    font-weight: 300;
    font-size: 17px;
    letter-spacing: 0.3px;
    display: flex;
    align-items: center;
    justify-content: center;
  }

  /* Brand side */
  .card--brand {
    left: 625px;
    background: var(--card-black);
    display: flex;
    align-items: center;
    justify-content: center;
  }
  .brand-name {
    color: var(--white);
    font-weight: 900;
    font-size: 52px;
    letter-spacing: 1px;
    text-transform: uppercase;
  }
</style>
</head>
<body>
  <main class="stage">
    <section class="card card--details" aria-label="Business card, details side">
      <div class="kitchen-photo" role="img" aria-label="Photo of a finished modern white kitchen with pendant lights"></div>
      <div class="details">
        <p class="details__name">Ruairi Dempsey</p>
        <p class="details__role">Director</p>
        <div class="details__rule"></div>
        <p class="details__phone">042 751 6092</p>
        <p class="details__email">ruairidempsey@tprservices-example.com.au</p>
      </div>
      <div class="services-band">Kitchen Installations/ Carpentry / Labour Hire</div>
    </section>

    <section class="card card--brand" aria-label="Business card, brand side">
      <p class="brand-name">TPR Services</p>
    </section>
  </main>
</body>
</html>
```